Dietitian needs a new business card design

I need a new business card design for my nutrition business that provides individual clinical nutrition advice for people with medical conditions. Business cards will be handed out to doctors, specialists and clients so will need to be sharp and project an image of professionalism

Target Market(s)

My clients are typically referred by doctors or specialists and the card will be used to handout to clients and their doctors.

Industry/Entity Type

Medical

Contact Information for Business Card

The business card will require the details below. These details can be found from my website https://www.tamberlydietitian.com.au/

Font styles to use
Serif

Colors

Designer to choose colors to be used in the design.

Requirements
Must have
• 1. It needs be professional and contemporary
• 2. It needs to incorporate my logo
• 3. It needs space to write appointment times and dates
• 4. It needs to provide my phone number, fax number, email address and my web address
Nice to have
• Include the Endorsed Clinical Dietitian Logo
• I have access to Pixorra if required
• The locations I practise from
Should not have
• Pictures of food
• Spelling MIstakes

```html
<!DOCTYPE html>
<html lang="en">
<head>
<meta charset="utf-8">
<title>Tamberly Nutrition &amp; Dietetics – Business Card</title>
<link href="https://fonts.googleapis.com/css2?family=Lato:wght@400;700&display=swap" rel="stylesheet">
<style>
  :root {
    --brand-blue: #0a5fb4;
    --brand-blue-light: #1a74c9;
    --accent-green: #7cc242;
    --accent-orange: #f47a20;
    --ink: #333b44;
    --paper: #ffffff;
    --backdrop: #d9d6d2;
  }
  * { box-sizing: border-box; margin: 0; padding: 0; }
  html, body { width: 1200px; height: 930px; overflow: hidden; }
  body {
    background: var(--backdrop);
    font-family: "Lato", sans-serif;
    color: var(--ink);
    position: relative;
  }
  .card {
    position: absolute;
    width: 560px;
    height: 320px;
    background: var(--paper);
    border-radius: 16px;
    overflow: hidden;
    box-shadow: 0 8px 18px rgba(0,0,0,0.22);
  }

  /* Appointment side */
  .card-front { left: 90px; top: 90px; }
  .front-band {
    position: absolute; inset: 0;
    background: linear-gradient(120deg, var(--brand-blue) 0%, var(--brand-blue-light) 55%, var(--brand-blue) 100%);
    clip-path: polygon(0 0, 100% 0, 100% 34%, 0 76%);
  }
  .front-brand {
    position: absolute; left: 150px; top: 45px;
    display: flex; align-items: center; gap: 16px;
    color: var(--paper);
  }
  .brand-dot {
    width: 64px; height: 64px; border-radius: 50%;
    background: currentColor; flex: none;
  }
  .brand-name { font-weight: 400; line-height: 1; }
  .brand-name .brand-main { display: block; font-size: 48px; letter-spacing: 0.5px; }
  .brand-name .brand-sub { display: block; font-size: 17px; margin-top: 4px; letter-spacing: 0.5px; }

  .appointment-title {
    position: absolute; left: 0; right: 0; top: 188px;
    text-align: center; font-size: 19px; color: var(--brand-blue);
  }
  .write-field {
    position: absolute; display: flex; align-items: flex-end; gap: 8px;
    font-size: 19px; color: #222;
  }
  .write-field .line { flex: 1; border-bottom: 1.5px solid #222; height: 1px; margin-bottom: 5px; }
  .field-date { left: 300px; right: 30px; top: 228px; }
  .field-time { left: 30px; right: 280px; top: 268px; }

  /* Contact side */
  .card-back { left: 560px; top: 490px; }
  .name-band {
    position: absolute; left: 0; top: 110px; width: 330px; height: 78px;
    background: var(--brand-blue);
    clip-path: polygon(0 0, 100% 0, 82% 100%, 0 100%);
    color: var(--paper);
    padding: 14px 0 0 34px;
  }
  .person-name { font-size: 24px; font-weight: 700; letter-spacing: 0.5px; }
  .person-role { font-size: 16px; margin-top: 2px; }

  .back-brand {
    position: absolute; left: 300px; top: 80px;
    display: flex; align-items: center; gap: 12px;
    color: var(--brand-blue);
  }
  .back-brand .brand-dot { width: 54px; height: 54px; }
  .back-brand .brand-main { font-size: 38px; }
  .back-brand .brand-sub { font-size: 14px; }

  .credential-badge {
    position: absolute; right: 36px; top: 26px;
    width: 130px; height: 62px; border-radius: 6px;
    background: var(--accent-orange);
  }

  .address {
    position: absolute; right: 34px; top: 210px;
    text-align: right; font-size: 15px; line-height: 1.35;
  }

  .contact-list {
    position: absolute; left: 120px; top: 212px;
    list-style: none; font-size: 15px; line-height: 1.4;
  }
  .contact-list li { display: flex; align-items: center; gap: 10px; }
  .contact-list svg { width: 13px; height: 13px; fill: var(--brand-blue); flex: none; }
  .contact-list .web-host { color: var(--accent-green); }
</style>
</head>
<body>

  <section class="card card-front" aria-label="Appointment card">
    <div class="front-band"></div>
    <div class="front-brand">
      <span class="brand-dot" aria-hidden="true"></span>
      <span class="brand-name">
        <span class="brand-main">Tamberly</span>
        <span class="brand-sub">Nutrition &amp; Dietetics</span>
      </span>
    </div>
    <p class="appointment-title">Appointment</p>
    <div class="write-field field-date"><span>Date</span><span class="line"></span></div>
    <div class="write-field field-time"><span>Time</span><span class="line"></span></div>
  </section>

  <section class="card card-back" aria-label="Contact card">
    <div class="name-band">
      <p class="person-name">DANIEL REEVE</p>
      <p class="person-role">Director</p>
    </div>
    <div class="back-brand">
      <span class="brand-dot" aria-hidden="true"></span>
      <span class="brand-name">
        <span class="brand-main">Tamberly</span>
        <span class="brand-sub">Nutrition &amp; Dietetics</span>
      </span>
    </div>
    <div class="credential-badge" role="img" aria-label="Professional credential badge"></div>

    <p class="address">4/118 Kellaway Road<br>Ravenbrook Tasmania 7260</p>

    <ul class="contact-list">
      <li>
        <svg viewBox="0 0 16 16" aria-hidden="true"><path d="M3.5 1l2.5 3-1.5 2c1 2 3 4 5 5l2-1.5 3 2.5-1.5 2.5C7 15 1 9 1 2.5z"/></svg>
        0412 555 019
      </li>
      <li>
        <svg viewBox="0 0 16 16" aria-hidden="true"><path d="M4 1h8v4H4zM1 6h14v6h-3v3H4v-3H1zm4 4v4h6v-4z"/></svg>
        +613 5550 1827
      </li>
      <li>
        <svg viewBox="0 0 16 16" aria-hidden="true"><path d="M1 3h14v10H1zm1.5 1.5v.4L8 9l5.5-4.1v-.4zm0 2.3v4.7h11V6.8L8 10.9z"/></svg>
        daniel@tamberlydietitian.com.au
      </li>
      <li>
        <svg viewBox="0 0 16 16" aria-hidden="true"><circle cx="8" cy="8" r="7"/></svg>
        <span>www.<span class="web-host">tamberlydietitian</span>.com.au</span>
      </li>
    </ul>
  </section>

</body>
</html>
```